Birthday Card Designs

We are looking for multiple "Happy Birthday" Card designs. We only require the Front Image of the Card!

The cards are to be fun and joyous.
It can be funny, sweet or a mix.Please make the style current, modern, and clean. Outdated/old-looking designs are not what we are after.

We are awarding $100 per card design. We have set the project at 3 winners, though we will look to increase this to more if we like more designs.

Audience: Men and women
Age: 18+
Rating: Clean and family friendly
Colour Scheme: Bright and eye-catching

NOTE: This is my first brief with Art Meadow, and i have opted not to guarantee that I will acquire a design. If all goes well this round, this will definitely change in the future
Updates

Hi Designers,

This is my first time with Art Meadow, and so I'm unsure as to how impressive the quality of submissions can be. This is why the project is not guaranteed.

If this round goes well i will definitely guarantee in the future....

Thanks:)

Reason: To gain a few more entries, I've extended the deadline. I'm hoping for more illustrated content and cool typography, as opposed to simple graphics:) Thanks!

Target Market(s)

Males and Females

Industry/Entity Type

Crowd

Requirements
Must have
• The text/copy is up to the designer, but must include the word Birthday.
Nice to have
• Clean; Current; Conceptual; Cute; Funny; Sweet
Should not have
• Old Look; Dated Ideas; Ancient colour schemes; bad typography

```html
<!DOCTYPE html>
<html lang="en">
<head>
<meta charset="utf-8">
<title>Birthday Card – Keep Calm &amp; Enjoy</title>
<link rel="stylesheet" href="https://fonts.googleapis.com/css2?family=Josefin+Sans:wght@600;700&family=Poiret+One&family=Gelasio:wght@500&display=swap">
<style>
  :root {
    --page-bg: #ffffff;
    --label-grey: #a9a9a9;
    --ink: #2d2826;
    --sun-yellow: #f4c02e;
    --flame-orange: #f06812;
    --cream: #e7d79a;
    --leaf-green: #74b676;
    --sea-teal: #4cbdc6;
    --sky-blue: #4ba7dc;
    --rust: #c0401c;
  }
  html, body {
    margin: 0;
    padding: 0;
    width: 1200px;
    height: 1000px;
    overflow: hidden;
    background: var(--page-bg);
  }
  .sheet {
    position: relative;
    width: 1200px;
    height: 1000px;
  }
  .side-label {
    position: absolute;
    margin: 0;
    font-family: "Gelasio", Georgia, serif;
    font-size: 38px;
    font-weight: 500;
    color: var(--label-grey);
    line-height: 1;
  }
  .side-label--front { left: 92px; top: 95px; }
  .side-label--back { left: 1036px; top: 893px; }

  .card {
    position: absolute;
    top: 155px;
    width: 504px;
    height: 714px;
    overflow: hidden;
    background:
      radial-gradient(ellipse 60% 35% at 100% 0%, var(--flame-orange) 0%, rgba(240,104,18,0) 100%),
      radial-gradient(ellipse 55% 30% at 100% 62%, rgba(70,150,70,0.55) 0%, rgba(70,150,70,0) 100%),
      radial-gradient(ellipse 60% 30% at 0% 100%, var(--sky-blue) 0%, rgba(75,167,220,0) 100%),
      linear-gradient(180deg, var(--sun-yellow) 0%, #f2c640 22%, var(--cream) 52%, #b8cf8a 68%, var(--leaf-green) 80%, var(--sea-teal) 100%);
  }
  .card--front { left: 62px; }
  .card--back { left: 614px; }

  .emblem {
    position: absolute;
    left: 181px;
    top: 2px;
    width: 110px;
    height: 178px;
    border-radius: 8px;
    background: linear-gradient(180deg, var(--rust), #a8361a);
    opacity: 0.85;
  }

  .headline {
    position: absolute;
    left: 0;
    width: 100%;
    margin: 0;
    text-align: center;
    color: var(--ink);
    line-height: 1;
    white-space: nowrap;
  }
  .headline--bold { font-family: "Josefin Sans", "Trebuchet MS", sans-serif; font-weight: 600; }
  .headline--thin { font-family: "Poiret One", "Helvetica Neue", sans-serif; font-weight: 400; }

  .keep-calm { top: 222px; font-size: 79px; letter-spacing: -3px; left: -4px; }
  .ampersand { top: 287px; font-size: 48px; left: -26px; }
  .enjoy { top: 351px; font-size: 95px; letter-spacing: 6px; left: 3px; }
  .your { top: 455px; font-size: 60px; left: -9px; }
  .birthday { top: 525px; font-size: 64px; letter-spacing: 1px; left: 0; }
  .party { top: 591px; font-size: 86px; left: 11px; }

  .back-line { text-align: left; width: auto; }
  .wish { left: 63px; top: 553px; font-size: 46px; }
  .you { left: 70px; top: 604px; font-size: 46px; }
  .the-best { left: 14px; top: 658px; font-size: 44px; letter-spacing: -1px; }
</style>
</head>
<body>
<main class="sheet">
  <p class="side-label side-label--front">front</p>

  <section class="card card--front" aria-label="Card front">
    <div class="emblem" role="img" aria-label="Crown above three beer bottles"></div>
    <h1 class="headline headline--bold keep-calm">KEEP CALM</h1>
    <p class="headline headline--bold ampersand">&amp;</p>
    <p class="headline headline--bold enjoy">ENJOY</p>
    <p class="headline headline--thin your">YOUR</p>
    <p class="headline headline--bold birthday">BIRTHDAY</p>
    <p class="headline headline--bold party">PARTY!</p>
  </section>

  <section class="card card--back" aria-label="Card back">
    <p class="headline headline--bold back-line wish">WISH</p>
    <p class="headline headline--thin back-line you">YOU</p>
    <p class="headline headline--bold back-line the-best">THE BEST!</p>
  </section>

  <p class="side-label side-label--back">back</p>
</main>
</body>
</html>
```